Web interface for PC desktop app

We need an HTML design for our new PC software.

To get an idea of the project scope, please review the interface draft in the attached files. The screenshot shows almost all dialogs of our product.

Our product is software that allows users to replace static Windows wallpaper with live animated scenes. The program interface consists of a gallery where users can select and download animated scenes, as well as an information area with scene details and current desktop settings. The product will be distributed on the Vexlo platform among the gamer community.

For this project, you need to create an engaging and user-friendly interface using HTML and CSS in two color schemes (black and white). Additionally, you will need to create a colorized version of the main program icon in vector format (a draft of the program icon is attached), design all other program icons, including icons for the title bar, and redraw all other images according to your design style.

Project Requirements:
-Develop a comprehensive design for the application, including icons and images, in two color schemes: dark and light.
-Colorize our main program icon according to your design style.
-Create other UI icons in all sizes from 16x16 to 512x512 pixels, ensuring that other images are suitable for up to 4K monitors.
-Ensure all UI controls have styles for standard Windows states: normal, hovered, active, and disabled.

Deliverables:
-Final design in HTML and CSS format.
-Icons in ICO format.
-Images in PNG format.

• all interface elements, including the program title bar, coded in HTML and CSS.

```html
<!DOCTYPE html>
<html lang="en">
<head>
<meta charset="utf-8">
<title>Paneora – Wallpaper Workshop</title>
<link href="https://fonts.googleapis.com/css2?family=Red+Hat+Display:wght@400;500;700&family=Red+Hat+Text:wght@400;500&display=swap" rel="stylesheet">
<style>
:root{
  --bg:#111a54;
  --band:rgba(255,255,255,.05);
  --titlebar:#0b1237;
  --panel-left:#121b57;
  --panel-right:#19236a;
  --chip:#1d2873;
  --chip-dark:#0e1645;
  --divider:#2c3784;
  --text:#ffffff;
  --muted:#8d96c9;
  --muted-2:#aab1dc;
  --yellow-a:#f9d348;
  --yellow-b:#fbe595;
  --blue-a:#3f7ef0;
  --blue-b:#14b1f6;
  --bar-blue:#1aa8f5;
  --star:#ffc21a;
  --heart:#f03a3a;
}
*{box-sizing:border-box;margin:0;padding:0}
html,body{width:1200px;height:784px;overflow:hidden}
body{background:var(--bg);font-family:"Red Hat Text",sans-serif;color:var(--text);position:relative}
.abs{position:absolute}
.backdrop{position:absolute;inset:0}

/* icon tiles */
.tile{position:absolute;left:70px;width:175px;height:150px;border-radius:30px;display:flex;align-items:center;justify-content:center;font-family:"Red Hat Display",sans-serif;font-weight:500;font-size:26px}
.tile-yellow{top:55px;background:linear-gradient(90deg,var(--yellow-a),var(--yellow-b));color:#fff}
.tile-blue{top:305px;background:linear-gradient(160deg,var(--blue-a),var(--blue-b));color:#fff}
.tile-outline{top:537px;border:2px solid #fff;color:#fff}
.tile-bar{position:absolute;left:117px;width:81px;height:12px;border-radius:6px}
.bar-yellow{top:218px;background:var(--yellow-a)}
.bar-blue{top:468px;background:var(--bar-blue)}
.bar-outline{top:700px;border:2px solid #fff}

/* window */
.window{position:absolute;left:374px;top:108px;width:826px;height:676px;overflow:hidden}
.titlebar{height:53px;background:var(--titlebar);display:flex;align-items:center;padding-left:26px;gap:8px}
.app-mark{width:27px;height:27px;border-radius:6px;background:linear-gradient(160deg,#6a7df5,#3f52d8)}
.app-name{font-family:"Red Hat Display",sans-serif;font-size:17px;font-weight:500}
.panel-left{position:absolute;left:0;top:53px;width:334px;bottom:0;background:var(--panel-left)}
.panel-right{position:absolute;left:334px;top:53px;right:0;bottom:0;background:var(--panel-right)}

.tabs{position:absolute;left:39px;top:26px;display:flex;align-items:center;font-family:"Red Hat Display",sans-serif;font-size:16px}
.tab{display:flex;align-items:center;gap:9px}
.tab-off{color:var(--muted)}
.tab-sep{width:1px;height:24px;background:var(--divider);margin:0 20px}

.screen{position:absolute;border-radius:8px}
.screen-active{left:25px;top:73px;width:139px;height:94px;background:var(--chip)}
.monitor{position:absolute;border:2px solid #050a20;border-radius:2px}
.monitor-base{position:absolute;height:2px;background:#5b66a8;border-radius:1px}

.meta{position:absolute;left:25px;font-size:12px;color:var(--muted)}
.meta b{font-weight:400;color:var(--text);margin-left:4px}

.btn{position:absolute;height:26px;border-radius:13px;background:var(--chip);display:flex;align-items:center;gap:6px;padding:0 11px;font-size:12.5px;color:#e6e9ff}
.btn svg{flex:none}
.btn-round{width:26px;padding:0;justify-content:center}

.hr{position:absolute;left:0;width:334px;top:416px;height:1px;background:var(--divider)}

.art{position:absolute;overflow:hidden}
.art-lake{background:linear-gradient(180deg,#6f7fa8 0%,#c98ea6 35%,#4a5f86 62%,#2c3d63 100%)}
.art-sunset{background:linear-gradient(180deg,#2a2140 0%,#7a2c2a 45%,#e0642a 70%,#3b2030 100%)}
.art-storm{background:linear-gradient(180deg,#5d6055 0%,#3d413b 55%,#22261f 100%)}
.art-fire{background:linear-gradient(180deg,#3a2a2c 0%,#7a3a26 50%,#1e2436 100%)}
.stars{position:absolute;left:11px;top:6px;font-size:16px;letter-spacing:1px;color:var(--star)}
.stars i{font-style:normal;color:#fff}
.fav{position:absolute;width:26px;height:26px;border-radius:50%;display:flex;align-items:center;justify-content:center}
.fav-dark{background:#16205e}
.fav-light{background:#fff}

.card-title{position:absolute;font-family:"Red Hat Display",sans-serif;font-weight:700;font-size:14.5px;letter-spacing:.2px}
.card-by{position:absolute;font-size:12px;color:var(--muted-2)}
.card-spec{position:absolute;font-size:12px;text-align:right;color:#e6e9ff;line-height:20px}

.seg{position:absolute;top:25px;display:flex;align-items:center;gap:6px;height:27px;padding:0 7px;font-size:12.5px;color:#dfe3ff}
.seg-active{background:var(--chip-dark)}
.pill{position:absolute;top:82px;height:42px;border-radius:21px;background:var(--chip);display:flex;align-items:center;gap:12px;padding-left:20px;font-size:13.5px;color:#fff}
</style>
</head>
<body>

<svg class="backdrop" width="1200" height="784" aria-hidden="true">
  <path d="M95 0 Q170 180 350 320 T374 420" fill="none" stroke="var(--band)" stroke-width="36"/>
  <path d="M320 0 Q370 60 410 108" fill="none" stroke="var(--band)" stroke-width="30"/>
  <path d="M1020 0 Q960 60 900 108" fill="none" stroke="var(--band)" stroke-width="30"/>
</svg>

<div class="tile tile-yellow">Paneora</div>
<div class="tile-bar bar-yellow"></div>
<div class="tile tile-blue">Paneora</div>
<div class="tile-bar bar-blue"></div>
<div class="tile tile-outline">Paneora</div>
<div class="tile-bar bar-outline"></div>

<main class="window">
  <header class="titlebar">
    <span class="app-mark"></span>
    <span class="app-name">Paneora</span>
  </header>

  <section class="panel-left">
    <nav class="tabs">
      <span class="tab">
        <svg width="18" height="18" viewBox="0 0 18 18" fill="none" stroke="#fff" stroke-width="1.6"><path d="M2 6V2h4M12 2h4v4M16 12v4h-4M6 16H2v-4"/><path d="M5 12l3-3 2 2 3-3"/></svg>
        Wallpapers
      </span>
      <span class="tab-sep"></span>
      <span class="tab tab-off">
        <svg width="20" height="18" viewBox="0 0 20 18" fill="none" stroke="currentColor" stroke-width="1.5"><rect x="1.5" y="2" width="17" height="11" rx="1.5"/><path d="M7 16h6M10 13v3"/></svg>
        ScreenSavers
      </span>
    </nav>

    <div class="screen screen-active"></div>
    <div class="monitor art art-lake" style="left:44px;top:85px;width:102px;height:67px" role="img" aria-label="Wallpaper preview: red tree on a cliff under a blue sky"></div>
    <div class="monitor-base" style="left:31px;top:154px;width:128px"></div>
    <div class="monitor art" style="left:196px;top:89px;width:91px;height:59px;background:linear-gradient(180deg,#2c7fae,#6fd3e6 50%,#1b3f72)" role="img" aria-label="Wallpaper preview: figure beneath a full moon"></div>
    <div class="monitor-base" style="left:185px;top:150px;width:110px"></div>

    <p class="meta" style="top:204px">Display 1: <b>Vista Q24</b></p>
    <p class="meta" style="top:229px">Wallpaper: <b>System Default</b></p>

    <div class="btn" style="left:25px;top:257px">
      <svg width="14" height="14" viewBox="0 0 14 14" fill="none" stroke="#fff" stroke-width="1.5"><circle cx="7" cy="7" r="2"/><circle cx="7" cy="7" r="5" stroke-dasharray="2 1.4"/></svg>Settings</div>
    <div class="btn" style="left:121px;top:257px">
      <svg width="15" height="14" viewBox="0 0 15 14" fill="none" stroke="#fff" stroke-width="1.5"><rect x="1" y="1.5" width="12" height="8.5" rx="1"/><path d="M5 13h4M9 8l3 3"/></svg>Next</div>
    <div class="btn" style="left:198px;top:257px">
      <svg width="15" height="12" viewBox="0 0 15 12" fill="none" stroke="#fff" stroke-width="1.5"><rect x="1" y="1.5" width="13" height="9"/><path d="M1 4h13"/></svg>View</div>
    <div class="btn btn-round" style="left:274px;top:257px">
      <svg width="4" height="14" viewBox="0 0 4 14" fill="#fff"><circle cx="2" cy="2" r="1.4"/><circle cx="2" cy="7" r="1.4"/><circle cx="2" cy="12" r="1.4"/></svg></div>

    <div class="hr"></div>

    <div class="art art-lake" style="left:26px;top:444px;width:283px;height:180px" role="img" aria-label="Artwork: red pagoda on a pier over a misty lake at sunset">
      <span class="stars">★★★★<i>★</i></span>
      <span class="fav fav-light" style="right:11px;top:17px"><svg width="14" height="12" viewBox="0 0 14 12"><path d="M7 11.5 1.5 6A3.2 3.2 0 0 1 7 2a3.2 3.2 0 0 1 5.5 4z" fill="var(--heart)"/></svg></span>
    </div>
    <h2 class="card-title" style="left:26px;top:643px">Japan digital art</h2>
    <p class="card-by" style="left:26px;top:664px">by: Paneora</p>
    <p class="card-spec" style="left:194px;top:641px;text-align:left"><span style="color:var(--muted)">Image Size:</span>&nbsp; 5.4Mb<br><span style="color:var(--muted)">Resolution:</span>&nbsp; 3480x2300</p>

    <div class="btn" style="left:26px;top:689px;height:30px;border-radius:15px;padding:0 13px">
      <svg width="14" height="12" viewBox="0 0 14 12" fill="none" stroke="#fff" stroke-width="1.6"><path d="M1 6.5 5 10.5 13 1.5"/></svg>Apply</div>
    <div class="btn" style="left:125px;top:689px;height:30px;border-radius:15px;padding:0 13px">
      <svg width="15" height="12" viewBox="0 0 15 12" fill="none" stroke="#fff" stroke-width="1.5"><rect x="1" y="1" width="13" height="4"/><path d="M1 8h13M1 11h13"/></svg>Try</div>
    <div class="btn" style="left:200px;top:689px;height:30px;border-radius:15px;padding:0 13px">
      <svg width="14" height="14" viewBox="0 0 14 14" fill="none" stroke="#fff" stroke-width="1.5"><rect x="1" y="1" width="12" height="12" rx="1.5"/><path d="M4 7h6"/></svg>Uninstall</div>
    <div class="btn btn-round" style="left:280px;top:689px;width:30px;height:30px;border-radius:15px">
      <svg width="4" height="14" viewBox="0 0 4 14" fill="#fff"><circle cx="2" cy="2" r="1.4"/><circle cx="2" cy="7" r="1.4"/><circle cx="2" cy="12" r="1.4"/></svg></div>
  </section>

  <section class="panel-right">
    <div class="seg" style="left:38px">
      <svg width="15" height="15" viewBox="0 0 15 15" fill="none" stroke="#fff" stroke-width="1.5"><rect x="1" y="1.5" width="13" height="12" rx="1.5"/><path d="M7.5 3.5v6M5 7l2.5 2.5L10 7"/></svg>Installed</div>
    <div class="seg seg-active" style="left:120px">
      <svg width="16" height="14" viewBox="0 0 16 14" fill="none" stroke="#4d74ff" stroke-width="1.6"><rect x="1" y="1" width="14" height="9.5" rx="1"/><path d="M5 13h6"/></svg>Workshop</div>

    <div class="pill" style="left:29px;width:265px">
      <svg width="18" height="18" viewBox="0 0 18 18" fill="none" stroke="#fff" stroke-width="1.6"><circle cx="7.5" cy="7.5" r="6"/><path d="M12 12l5 5"/></svg>Search for Wallpapers</div>
    <div class="pill" style="left:311px;width:113px;padding-left:22px">
      <svg width="16" height="18" viewBox="0 0 16 18" fill="none" stroke="#fff" stroke-width="1.5"><circle cx="8" cy="5" r="3.5"/><path d="M1.5 17c0-4 3-6 6.5-6s6.5 2 6.5 6z"/></svg>Creator</div>
    <div class="pill" style="left:442px;width:60px;padding-left:18px">
      <svg width="14" height="14" viewBox="0 0 14 14" fill="none" stroke="#fff" stroke-width="1.5"><rect x="1" y="1" width="5" height="5"/><rect x="8" y="1" width="5" height="5"/><rect x="1" y="8" width="5" height="5"/><rect x="8" y="8" width="5" height="5"/></svg></div>

    <div class="art art-lake" style="left:29px;top:156px;width:259px;height:155px" role="img" aria-label="Artwork: red pagoda on a pier over a misty lake at sunset">
      <span class="stars">★★★★<i>★</i></span>
      <span class="fav fav-dark" style="right:17px;top:15px"><svg width="13" height="11" viewBox="0 0 14 12"><path d="M7 11.5 1.5 6A3.2 3.2 0 0 1 7 2a3.2 3.2 0 0 1 5.5 4z" fill="#fff"/></svg></span>
    </div>
    <h3 class="card-title" style="left:29px;top:327px">Japan digital art</h3>
    <p class="card-by" style="left:29px;top:349px">by: Paneora</p>
    <p class="card-spec" style="left:200px;top:324px;width:88px">5.4Mb<br>3480x2300</p>

    <div class="art art-sunset" style="left:305px;top:156px;width:200px;height:155px" role="img" aria-label="Artwork: silhouette under a large tree at a fiery sunset">
      <span class="stars">★★★★<i>★</i></span>
    </div>
    <h3 class="card-title" style="left:305px;top:327px">Japan digital art</h3>
    <p class="card-by" style="left:305px;top:349px">by: Paneora</p>

    <div class="art art-storm" style="left:29px;top:391px;width:259px;height:155px" role="img" aria-label="Artwork: warrior in a windswept grassy storm">
      <span class="stars">★★★★<i>★</i></span>
      <span class="fav fav-dark" style="right:17px;top:15px"><svg width="13" height="11" viewBox="0 0 14 12"><path d="M7 11.5 1.5 6A3.2 3.2 0 0 1 7 2a3.2 3.2 0 0 1 5.5 4z" fill="#fff"/></svg></span>
    </div>
    <h3 class="card-title" style="left:29px;top:562px">Japan digital art</h3>
    <p class="card-by" style="left:29px;top:584px">by: Paneora</p>
    <p class="card-spec" style="left:200px;top:559px;width:88px">5.4Mb<br>3480x2300</p>

    <div class="art art-fire" style="left:305px;top:391px;width:200px;height:155px" role="img" aria-label="Artwork: caped hero amid a burning city">
      <span class="stars">★★★★<i style="color:#fff">★</i></span>
    </div>
    <h3 class="card-title" style="left:305px;top:562px">Japan digital art</h3>
    <p class="card-by" style="left:305px;top:584px">by: Paneora</p>
  </section>
</main>

</body>
</html>
```